We need a business card design for a Dubai based company .

We need a business card for a Dubai based company called "Zernova Smoking Requisites Trading LLC". We mainly import Flavoured Tobacco products and Charcoal which is used for smoking in a Hookah/Shisha and distribute to the wholesalers and retailers. Logo file is attached herewith.

```html
<!DOCTYPE html>
<html lang="en">
<head>
<meta charset="utf-8">
<title>Zernova Business Card</title>
<link href="https://fonts.googleapis.com/css2?family=Montserrat:wght@400;500;700&display=swap" rel="stylesheet">
<style>
  :root {
    --backdrop: #1e1e1e;
    --card-white: #f3f3f3;
    --brand-red: #c2474b;
    --swoosh-dark: #2b2b2b;
    --ink-grey: #4a4a4a;
    --card-dark: #2c2c2c;
    --text-white: #ffffff;
  }
  * { margin: 0; padding: 0; box-sizing: border-box; }
  html, body { width: 1200px; height: 900px; overflow: hidden; }
  body {
    background: var(--backdrop);
    font-family: "Montserrat", sans-serif;
    position: relative;
  }
  .card {
    position: absolute;
    left: 250px;
    width: 700px;
    height: 400px;
    overflow: hidden;
  }
  .card-front { top: 35px; background: var(--card-white); }
  .card-back {
    top: 465px;
    background: var(--card-dark);
    border: 2px solid var(--brand-red);
  }
  .front-shape { position: absolute; inset: 0; }
  .holder {
    position: absolute;
    right: 36px;
    top: 28px;
    text-align: right;
  }
  .holder-name {
    color: var(--brand-red);
    font-weight: 700;
    font-size: 30px;
    letter-spacing: 0.5px;
  }
  .holder-title {
    color: var(--ink-grey);
    font-weight: 400;
    font-size: 17px;
    margin-top: 4px;
  }
  .contact-list {
    position: absolute;
    right: 36px;
    top: 160px;
    list-style: none;
    color: var(--text-white);
    font-size: 16px;
    text-align: right;
    line-height: 29px;
  }
  .contact-list li { display: flex; justify-content: flex-end; align-items: center; gap: 10px; }
  .contact-list svg { width: 15px; height: 15px; flex: none; }
  .contact-list .no-icon { padding-right: 25px; }
  .brand {
    position: absolute;
    left: 55px;
    top: 165px;
    display: flex;
    align-items: center;
    gap: 14px;
    color: var(--ink-grey);
    font-weight: 500;
  }
  .brand-square {
    width: 22px;
    height: 22px;
    background: var(--brand-red);
    flex: none;
  }
  .brand-name { font-size: 34px; letter-spacing: 6px; line-height: 1; }
  .brand-line { font-size: 9.5px; letter-spacing: 1.8px; margin-top: 8px; }
  .back-fill {
    position: absolute;
    inset: 0;
    background: linear-gradient(135deg, #303030, #262626);
  }
  .back-brand {
    position: absolute;
    right: 60px;
    bottom: 110px;
    display: flex;
    align-items: center;
    gap: 12px;
    color: var(--text-white);
    font-weight: 500;
  }
  .back-brand .brand-square { width: 16px; height: 16px; }
  .back-brand .brand-name { font-size: 26px; letter-spacing: 5px; }
  .back-brand .brand-line { font-size: 7.5px; letter-spacing: 1.4px; margin-top: 6px; }
</style>
</head>
<body>
  <section class="card card-front">
    <svg class="front-shape" viewBox="0 0 700 400" width="700" height="400">
      <path d="M0,400 L0,372 C200,360 310,320 380,215 C450,120 520,105 700,100 L700,400 Z" fill="#c2474b"/>
      <path d="M150,352 C270,330 330,290 370,215 C420,125 480,95 600,88" fill="none" stroke="#2b2b2b" stroke-width="5"/>
      <path d="M170,345 C285,322 340,282 378,212 C428,126 490,100 580,94" fill="none" stroke="#2b2b2b" stroke-width="3"/>
      <path d="M190,342 C300,318 350,280 386,215 C436,130 500,106 560,100" fill="none" stroke="#2b2b2b" stroke-width="2"/>
    </svg>

    <div class="brand">
      <span class="brand-square"></span>
      <div>
        <div class="brand-name">ZERNOVA</div>
        <div class="brand-line">SMOKING REQUISITES TRADING LLC</div>
      </div>
    </div>

    <div class="holder">
      <div class="holder-name">MARCUS HALE</div>
      <div class="holder-title">Managing Director</div>
    </div>

    <ul class="contact-list">
      <li>044-555 010 234
        <svg viewBox="0 0 16 16"><path d="M3 1 L6 1 L7 5 L5 6 C6 8 8 10 10 11 L11 9 L15 10 L15 13 C15 14 14 15 13 15 C7 15 1 9 1 3 C1 2 2 1 3 1 Z" fill="#fff"/></svg>
      </li>
      <li>info@zernovatrade.com
        <svg viewBox="0 0 16 16"><rect x="1" y="3" width="14" height="10" fill="#fff"/><path d="M1 3 L8 9 L15 3" fill="none" stroke="#c2474b" stroke-width="1.3"/></svg>
      </li>
      <li>www.zernovatrade.com
        <svg viewBox="0 0 16 16"><circle cx="8" cy="8" r="7" fill="#fff"/><path d="M1 8 H15 M8 1 C4 5 4 11 8 15 C12 11 12 5 8 1" fill="none" stroke="#c2474b" stroke-width="1"/></svg>
      </li>
      <li class="no-icon">421, Address line here</li>
      <li class="no-icon">Country Name, 45452</li>
    </ul>
  </section>

  <section class="card card-back">
    <div class="back-fill" role="img" aria-label="Dark card back with a faint repeating embossed brand-name pattern"></div>
    <div class="back-brand">
      <span class="brand-square"></span>
      <div>
        <div class="brand-name">ZERNOVA</div>
        <div class="brand-line">SMOKING REQUISITES TRADING LLC</div>
      </div>
    </div>
  </section>
</body>
</html>
```